Business card design for a engineering company

I need a double sided business card design for my company "Verdmont Flow Solutions". The card will be used in Malaysia. Sleek and professional, with a little design flare to it.
Information to showcase:
1. Company logo
2. Name, title, phone, email address, website address
3. our products "Pumping technology, Valve & actuation, Air Moving Technology
Example:
Ravi Tanaka
Business manager
ravi.tanaka@verdmont-example.com
www.verdmont-example.com.my
- Pumping technology
- Valve & actuation
- Air moving technology
Target Market(s)
engineers, purchasing managers
Industry/Entity Type
Business
Contact Information for Business Card
Ravi Tanaka
Business manager
ravi.tanaka@verdmont-example.com
www.verdmont-example.com.my
- Pumping technology
- Valve & actuation
- Air moving technology
catch phrase : "Solving flow challenges, exceeding expectations"

```html
<!DOCTYPE html>
<html lang="en">
<head>
<meta charset="utf-8">
<title>Verdmont Flow Solutions – Business Card</title>
<link rel="stylesheet" href="https://fonts.googleapis.com/css2?family=Source+Sans+3:ital,wght@0,400;0,600;0,700;1,400&display=swap">
<style>
  :root {
    --stage: #e9e9e7;
    --paper: #ffffff;
    --navy: #0c3346;
    --slate: #1f4152;
    --ink: #3a4a55;
    --orange: #f0922b;
    --amber: #f9c20f;
    --ember: #ec6a2c;
    --rule: #c9cfd3;
  }
  * { box-sizing: border-box; margin: 0; padding: 0; }
  html, body {
    width: 1200px; height: 987px; overflow: hidden;
    background: var(--stage);
    font-family: "Source Sans 3", "Myriad Pro", sans-serif;
  }
  .card {
    position: absolute; left: 293px; width: 615px; height: 350px;
    box-shadow: 0 4px 12px rgba(0,0,0,.18);
  }
  .card--front { top: 130px; background: var(--paper); }
  .card--back { top: 506px; background: var(--navy); color: #fff; }

  .brand {
    position: absolute; left: 40px; top: 157px;
    display: flex; align-items: center; gap: 12px;
  }
  .brand__dot { width: 38px; height: 38px; border-radius: 50%; background: var(--slate); }
  .brand__name { font-size: 18px; font-weight: 600; color: var(--slate); letter-spacing: .3px; }

  .divider {
    position: absolute; left: 303px; top: 104px; width: 1px; height: 148px;
    background: var(--rule);
  }

  .contact { position: absolute; left: 326px; top: 102px; }
  .contact__name { font-size: 23px; font-weight: 700; color: var(--slate); letter-spacing: 1px; }
  .contact__title { font-size: 18px; color: var(--orange); margin-top: 2px; margin-bottom: 14px; }
  .contact__line {
    display: flex; align-items: center; gap: 7px;
    font-size: 14.5px; color: var(--ink); line-height: 23px;
  }
  .contact__line svg { width: 14px; height: 14px; fill: var(--slate); flex: none; }

  .band { position: absolute; left: 0; bottom: 0; height: 22px; }
  .band--slate { width: 450px; background: var(--slate); }
  .band--flare { left: 453px; right: 0; background: linear-gradient(90deg, var(--ember), var(--amber) 55%, var(--ember)); }

  .emblem {
    position: absolute; left: 0; right: 0; top: 120px;
    display: flex; align-items: center; justify-content: center; gap: 14px;
  }
  .emblem__dot { width: 44px; height: 44px; border-radius: 50%; background: var(--orange); }
  .emblem__name { font-size: 34px; font-weight: 600; color: #fff; letter-spacing: .5px; }

  .tagline {
    position: absolute; left: 0; right: 0; top: 277px;
    text-align: center; font-size: 17px; font-style: italic;
  }
  .products {
    position: absolute; left: 0; right: 0; top: 300px;
    display: flex; justify-content: center; gap: 10px; font-size: 17px;
  }
  .products__sep { color: var(--orange); }
</style>
</head>
<body>
  <section class="card card--front">
    <div class="brand">
      <span class="brand__dot"></span>
      <span class="brand__name">Verdmont Flow Solutions</span>
    </div>
    <div class="divider"></div>
    <div class="contact">
      <p class="contact__name">RAVI TANAKA</p>
      <p class="contact__title">Business manager</p>
      <p class="contact__line">
        <svg viewBox="0 0 16 16"><path d="M3.6 1.2l2.3 2.9-1.3 1.8c.9 2 2.5 3.6 4.5 4.5l1.8-1.3 2.9 2.3-1.1 2.6C6.8 13.8 2.2 9.2 1 3.3z"/></svg>
        600 555 0142
      </p>
      <p class="contact__line">
        <svg viewBox="0 0 16 16"><path d="M1 3h14v10H1zm1.6 1.4L8 8.6l5.4-4.2z"/></svg>
        ravi.tanaka@verdmont-example.com
      </p>
      <p class="contact__line">
        <svg viewBox="0 0 16 16"><path d="M8 1a7 7 0 100 14A7 7 0 008 1zm-1 2.2c-1 1-1.6 2-1 3l2 .5.4 1.8-1.2 1.5.6 2.7C5 12.2 3 10.5 3 8c0-2.2 1.6-4.1 4-4.8zm3 .4c1.8.8 3 2.4 3 4.4l-1.8-.6-1.4 1-1.3-1.6 1.3-1.4z"/></svg>
        www.verdmont-example.com.my
      </p>
    </div>
    <div class="band band--slate"></div>
    <div class="band band--flare"></div>
  </section>

  <section class="card card--back">
    <div class="emblem">
      <span class="emblem__dot"></span>
      <span class="emblem__name">Verdmont</span>
    </div>
    <p class="tagline">Solving flow challenges, exceeding expectations</p>
    <p class="products">
      <span>Pumping technology</span><span class="products__sep">•</span>
      <span>Valve &amp; actuation</span><span class="products__sep">•</span>
      <span>Air moving technology</span>
    </p>
  </section>
</body>
</html>
```